Yard Sign Design Needed

Yard sign needed for mowing & landscaping company. Would like to use the top logo with black background which is attached. Would like MOWING to be in large standout letters. The word "landscaping" can be smaller and more artistic or omitted. Will need room for phone number once design is approved. The phone number will need to stand out and look identical/similar to the word 'MOWING"

```html
<!DOCTYPE html>
<html lang="en">
<head>
<meta charset="utf-8">
<title>Brantel Contractors – Mowing Yard Sign</title>
<link href="https://fonts.googleapis.com/css2?family=Anton&family=Montserrat:wght@600;800&display=swap" rel="stylesheet">
<style>
  :root {
    --page-bg: #ffffff;
    --sign-black: #070707;
    --lime: #bccb32;
    --white: #ffffff;
    --ink: #0a0a0a;
  }
  html, body {
    margin: 0;
    padding: 0;
    width: 1200px;
    height: 729px;
    overflow: hidden;
    background: var(--page-bg);
  }
  .canvas {
    position: relative;
    width: 1200px;
    height: 729px;
  }
  .yard-sign {
    position: absolute;
    left: 373px;
    top: 24px;
    width: 453px;
    height: 680px;
    box-shadow: -6px 6px 14px rgba(0, 0, 0, 0.35);
  }
  .yard-sign svg {
    display: block;
    width: 100%;
    height: 100%;
  }
  .sign-bg { fill: var(--sign-black); }
  .accent { fill: var(--lime); }
  .brand-mark { fill: var(--lime); }
  .brand-rule { stroke: var(--white); stroke-width: 1.5; }
  .brand-name {
    font-family: "Montserrat", sans-serif;
    font-weight: 600;
    fill: var(--white);
  }
  .headline {
    font-family: "Anton", sans-serif;
    fill: var(--white);
  }
  .subline {
    font-family: "Montserrat", sans-serif;
    font-weight: 800;
    fill: var(--ink);
  }
  .phone {
    font-family: "Anton", sans-serif;
    fill: var(--white);
  }
</style>
</head>
<body>
<main class="canvas">
  <section class="yard-sign" aria-label="Mowing yard sign for Brantel Contractors">
    <svg viewBox="0 0 787 1181" preserveAspectRatio="none">
      <rect class="sign-bg" x="0" y="0" width="787" height="1181"/>

      <polygon class="accent" points="0,50 400,616 0,261"/>
      <polygon class="accent" points="787,68 402,616 787,275"/>

      <rect class="brand-mark" x="344" y="80" width="100" height="100"/>
      <text class="brand-name" x="394.5" y="302" font-size="66" text-anchor="middle" textLength="303" lengthAdjust="spacingAndGlyphs">BRANTEL</text>
      <text class="brand-name" x="396" y="335" font-size="36" text-anchor="middle" textLength="310" lengthAdjust="spacingAndGlyphs">CONTRACTORS</text>
      <line class="brand-rule" x1="243" y1="351" x2="359" y2="351"/>
      <line class="brand-rule" x1="431" y1="351" x2="548" y2="351"/>
      <text class="brand-name" x="395" y="358" font-size="20" text-anchor="middle" letter-spacing="3">LLC</text>

      <text class="headline" x="63" y="823" font-size="196" textLength="661" lengthAdjust="spacingAndGlyphs">MOWING</text>

      <rect class="accent" x="0" y="858" width="787" height="60"/>
      <text class="subline" x="111" y="903" font-size="44" textLength="545" lengthAdjust="spacing">Landscaping</text>

      <text class="phone" x="47" y="1046" font-size="112" textLength="677" lengthAdjust="spacingAndGlyphs">00 987 654 32</text>
    </svg>
  </section>
</main>
</body>
</html>
```